Flyer Handout when attending Dental Conventions, or dental office shows

take the sample file folder that is shown with 2 pictures. The outside and inside of the folder needs to be completed, along with the inserts. This folder pictures are from someone elses flyer/folder and i would like to have it layout like this. The KPW inserts is informational, but it is lacking originality, pictures, etc. Try to make our information and move it to 2017. When this is done, i would like to take this flyer and load it to the web or allow to send via email and make it interactive. The user can select the flyers and it will slide or flip to the flyer. this will make if kewl/fun

Target Market(s)

Dental Offices

Industry/Entity Type

Dental

Font styles to use
Serif
Sans Serif

Colors

Designer to choose colors to be used in the design.

Requirements
Must have
• a Semi new look and feel of our flyers, and a new envelope created

```html
<!DOCTYPE html>
<html lang="en">
<head>
<meta charset="utf-8">
<title>KPW Pocket Folder – Flat Layout</title>
<link rel="stylesheet" href="https://fonts.googleapis.com/css2?family=Ubuntu:wght@300;400;500;700&display=swap">
<style>
  :root {
    --stage: #58595b;
    --paper: #ffffff;
    --brand-blue: #1e95d3;
    --brand-orange: #f39433;
    --pocket-grey: #d1d2d4;
    --frame-line: #9fd3ee;
    --die-red: #e8483b;
    --fold-green: #3bb54a;
    --text-blue: #1a8dd0;
  }
  * { margin: 0; padding: 0; box-sizing: border-box; }
  html, body { width: 1200px; height: 800px; overflow: hidden; background: var(--stage); }
  .canvas { position: relative; width: 1200px; height: 800px; font-family: "Ubuntu", sans-serif; }
  .dieline { position: absolute; inset: 0; }
  .brand-name {
    position: absolute; color: var(--brand-blue); font-weight: 700;
    letter-spacing: 1px; line-height: 1;
  }
  .brand-name--back { left: 204px; top: 70px; font-size: 44px; }
  .brand-name--front { left: 616px; top: 50px; font-size: 56px; }
  .contact-block {
    position: absolute; left: 182px; width: 403px; top: 493px;
    text-align: center; color: var(--text-blue); font-size: 13px;
    font-weight: 500; line-height: 16.5px;
  }
  .tagline {
    position: absolute; left: 637px; top: 495px; color: var(--text-blue);
    font-size: 17px; font-weight: 300; line-height: 22px;
  }
  .tagline strong { font-weight: 700; }
</style>
</head>
<body>
<div class="canvas">
  <svg class="dieline" width="1200" height="800" viewBox="0 0 1200 800" xmlns="http://www.w3.org/2000/svg">
    <defs>
      <linearGradient id="backCoverShade" x1="0" y1="1" x2="0.6" y2="0.3">
        <stop offset="0" stop-color="#e4e6e8"/>
        <stop offset="1" stop-color="#ffffff"/>
      </linearGradient>
      <linearGradient id="frontCoverShade" x1="0.7" y1="0" x2="1" y2="0">
        <stop offset="0" stop-color="#ffffff"/>
        <stop offset="1" stop-color="#e6e7e9"/>
      </linearGradient>
      <linearGradient id="smilePhoto" x1="0" y1="0" x2="1" y2="0">
        <stop offset="0" stop-color="#f3d6cc"/>
        <stop offset="0.45" stop-color="#f6e8e6"/>
        <stop offset="1" stop-color="#fbfbfb"/>
      </linearGradient>
      <linearGradient id="portraitTones" x1="0" y1="0" x2="0" y2="1">
        <stop offset="0" stop-color="#c79f86"/>
        <stop offset="1" stop-color="#eed2c6"/>
      </linearGradient>
    </defs>

    <!-- sheet -->
    <rect x="129" y="24" width="942" height="752" fill="var(--paper)"/>

    <!-- cover panels -->
    <rect class="back-cover" x="166" y="24" width="434" height="546" fill="url(#backCoverShade)"/>
    <rect class="front-cover" x="600" y="24" width="434" height="546" fill="url(#frontCoverShade)"/>

    <!-- inner safety frames -->
    <rect x="182" y="41" width="403" height="513" fill="none" stroke="var(--frame-line)" stroke-width="0.8"/>
    <rect x="615" y="41" width="404" height="513" fill="none" stroke="var(--frame-line)" stroke-width="0.8"/>

    <!-- back cover photo band -->
    <g role="img" aria-label="Close-up photo of a bright smile beside a dental mirror">
      <rect x="166" y="160" width="434" height="238" fill="url(#smilePhoto)"/>
    </g>
    <rect x="166" y="156" width="434" height="4" fill="var(--brand-blue)"/>
    <rect x="166" y="398" width="434" height="3" fill="var(--brand-blue)"/>

    <!-- front cover photo strips -->
    <rect x="600" y="162" width="52" height="236" fill="var(--brand-blue)"/>
    <g role="img" aria-label="Photo of a woman holding her cheek with toothache">
      <polygon points="661,162 764,162 748,424 642,424" fill="url(#portraitTones)"/>
    </g>
    <g role="img" aria-label="Photo of a child at a dental check-up with a mirror">
      <polygon points="788,113 890,113 860,474 752,474" fill="url(#portraitTones)"/>
    </g>
    <g role="img" aria-label="Photo of a laughing woman with a healthy smile">
      <polygon points="894,162 1000,162 978,398 872,398" fill="url(#portraitTones)"/>
    </g>
    <polygon points="1012,118 1034,118 1034,398 990,398" fill="var(--brand-orange)"/>

    <!-- pockets -->
    <rect x="168" y="572" width="29" height="202" fill="var(--pocket-grey)"/>
    <rect x="1003" y="572" width="29" height="202" fill="var(--pocket-grey)"/>
    <path class="pocket pocket--left" d="M206 586 H576 L556 730 Q550 758 522 758 H206 Z" fill="var(--brand-blue)"/>
    <path class="pocket pocket--right" d="M624 586 H994 V758 H678 Q650 758 644 730 Z" fill="var(--brand-blue)"/>

    <!-- card slits -->
    <g stroke="#ffffff" stroke-width="0.8">
      <line x1="300" y1="654" x2="327" y2="626"/>
      <line x1="435" y1="626" x2="463" y2="654"/>
      <line x1="300" y1="692" x2="327" y2="720"/>
      <line x1="435" y1="720" x2="463" y2="692"/>
    </g>

    <!-- fold lines -->
    <g stroke="var(--fold-green)" stroke-width="0.8" stroke-dasharray="3 3" fill="none">
      <line x1="166" y1="24" x2="166" y2="570"/>
      <line x1="600" y1="24" x2="600" y2="570"/>
      <line x1="1034" y1="24" x2="1034" y2="570"/>
    </g>
    <line x1="166" y1="570" x2="1034" y2="570" stroke="#e8e8e8" stroke-width="0.8" stroke-dasharray="3 3"/>

    <!-- cut lines -->
    <g stroke="var(--die-red)" stroke-width="0.9" fill="none">
      <path d="M166 30 L133 30 V350 A13 13 0 0 1 133 382 V550 L166 570"/>
      <path d="M1034 30 L1067 30 V350 A13 13 0 0 0 1067 382 V550 L1034 570"/>
      <path d="M168 570 V774 H540 Q566 774 574 744 L597 570"/>
      <path d="M1032 570 V774 H660 Q634 774 626 744 L603 570"/>
    </g>
  </svg>

  <div class="brand-name brand-name--back">KPW</div>
  <div class="brand-name brand-name--front">KPW</div>

  <address class="contact-block" style="font-style:normal">
    218 Harbor Lane, Ridgeford, MN 55190<br>
    Tel: 555-210-4470 | Fax: 555-210-4471<br>
    www.kpwdental.com
  </address>

  <p class="tagline">Bridging the Gap<br><strong>Between</strong> Payers &amp; Providers</p>
</div>
</body>
</html>
```